KZRM - Wave Banner Design

Please use the attached Wave Banner Template and KZRM logo and Tag Line and web URL to design a Corporate Banner.

Provide 2 options: one with a black background, one with a white background. Backgrounds should include the use of a subtle watermark to create texture and depth.

The design should position the Corporate Logo to highlight the corporate brand. The URL should be large enough to be read easily.

Colors
ec2027
ffffff

Requirements
Must have
• Use the font type provided.
Use Red and Argent only.
Provide a black background option and a white background option.
Should not have
• Do note change the combination of colours in the stripes.

```html
<!DOCTYPE html>
<html lang="en">
<head>
<meta charset="utf-8">
<title>KZRM – Wave Banner</title>
<link href="https://fonts.googleapis.com/css2?family=Orbitron:wght@600;700&display=swap" rel="stylesheet">
<style>
  :root {
    --brand-red: #ec2027;
    --argent: #c9ccd1;
    --banner-black: #333233;
    --banner-white: #ffffff;
    --stage: #ececec;
  }
  html, body {
    margin: 0;
    padding: 0;
    width: 1200px;
    height: 1000px;
    overflow: hidden;
    background: var(--stage);
  }
  .canvas {
    position: relative;
    width: 1200px;
    height: 1000px;
    font-family: "Orbitron", sans-serif;
  }
  .banner {
    position: absolute;
    top: 48px;
    width: 270px;
    height: 904px;
    box-sizing: border-box;
    text-align: center;
  }
  .banner--black {
    left: 298px;
    background: var(--banner-black);
    border-top-left-radius: 140px 200px;
    color: var(--argent);
  }
  .banner--white {
    left: 632px;
    background: var(--banner-white);
    border-top-right-radius: 140px 200px;
    color: var(--brand-red);
    box-shadow: 0 0 6px rgba(0,0,0,0.12);
  }
  .brand {
    position: absolute;
    top: 250px;
    left: 0;
    right: 0;
    display: flex;
    flex-direction: column;
    align-items: center;
    gap: 18px;
  }
  .brand__mark {
    width: 22px;
    height: 22px;
    background: currentColor;
  }
  .brand__name {
    font-size: 56px;
    font-weight: 700;
    letter-spacing: 3px;
    line-height: 1;
  }
  .tagline {
    position: absolute;
    top: 556px;
    left: 0;
    right: 0;
    margin: 0;
    font-size: 36px;
    font-weight: 600;
    letter-spacing: 4px;
    line-height: 58px;
  }
  .url {
    position: absolute;
    top: 868px;
    left: 0;
    right: 0;
    margin: 0;
    font-size: 16px;
    font-weight: 700;
    letter-spacing: 1.5px;
  }
  .banner--black .url { top: 822px; }
  .banner--white .url { top: 822px; }
</style>
</head>
<body>
  <main class="canvas">
    <section class="banner banner--black" aria-label="Black background option">
      <div class="brand">
        <span class="brand__mark"></span>
        <span class="brand__name">KZRM</span>
      </div>
      <p class="tagline">EARN<br>YOUR<br>STRIPES</p>
      <p class="url">WWW.KZRM.COM.AU</p>
    </section>

    <section class="banner banner--white" aria-label="White background option">
      <div class="brand">
        <span class="brand__mark"></span>
        <span class="brand__name">KZRM</span>
      </div>
      <p class="tagline">EARN<br>YOUR<br>STRIPES</p>
      <p class="url">WWW.KZRM.COM.AU</p>
    </section>
  </main>
</body>
</html>
```